Retail healthy snack bar design

We are launching a new product range to be sold in health food stores.

The Fennick Co (no logo as yet).

We will have a range of bars, spreads (jars), shakes (bags) in the following ranges-
milk protein
plant protein
keto

For this project, please do a bar design. The chosen designer will be given additional work for the rest of the packaging as well as promotional material such as social media, banners, posters etc.

Lumo Bar Protein - Must be White to be recognized.
Lumo Bar Collagen - Bronze
Lumo Keto Bar - Possibly Red
Lumo Bar Plant - Green

Food images can be added but their must be samples without as we may need to remove for certain countries.

Target Market(s)

Healthy, Weight-loss, Bodybuilding, Elderly, Medical

Industry/Entity Type

Health And Wellness

Font styles to use
Sans Serif

Colors

Designer to choose colors to be used in the design.

Requirements
Must have
• Clean simple to read design with minimal colours

Flavour to be easily read (Must include the word 'Flavour' in the same size font as the flavour description)

Must show size of bar (60g).

Some details that can be added (optional)-
raw, cold pressed bar with (example) whey protein isolate + prebiotic fibre
natural, with no artificial colours, flavours, preservatives or sweeteners
no added sugar or sugar alcohols - gluten free - soy free

Rear of bar shall remain the same or all same details if redesigned.
Nice to have
• Clean design, use of silver foil and/or matt/gloss affect, large oversized flavour image (if including).

See images of current designs I like on the market for ideas
Should not have
• Too many images (if any).

```html
<!DOCTYPE html>
<html lang="en">
<head>
<meta charset="utf-8">
<title>Banana Bread Flavour – Lumo Keto Bar</title>
<link rel="stylesheet" href="https://fonts.googleapis.com/css2?family=Lato:wght@400&display=swap">
<style>
  :root {
    --panel-grey: #dcdddd;
    --brand-blue: #0a8bd3;
    --ink: #231f20;
    --rule: #8a8a8a;
    --frame: #3a3a3a;
    --white: #ffffff;
  }
  html, body {
    margin: 0;
    padding: 0;
    width: 1200px;
    height: 464px;
    overflow: hidden;
    background: var(--white);
  }
  .wrapper {
    position: relative;
    width: 1200px;
    height: 464px;
    box-sizing: border-box;
    border: 1px solid var(--frame);
    display: flex;
    font-family: "Lato", Arial, sans-serif;
    font-weight: 400;
    color: var(--ink);
  }
  .info-panel {
    position: relative;
    width: 847px;
    height: 100%;
    background: var(--panel-grey);
  }
  .flavour-name {
    position: absolute;
    left: 47px;
    top: 46px;
    margin: 0;
    font-size: 50px;
    font-weight: 400;
    line-height: 1;
    white-space: nowrap;
  }
  .product-claims {
    position: absolute;
    left: 47px;
    top: 113px;
    margin: 0;
    font-size: 30px;
    line-height: 43px;
    white-space: nowrap;
  }
  .divider {
    position: absolute;
    left: 47px;
    top: 364px;
    width: 754px;
    height: 0;
    border-top: 1px solid var(--rule);
  }
  .nutrition-row {
    position: absolute;
    left: 47px;
    top: 368px;
    width: 754px;
    height: 56px;
    display: flex;
    align-items: baseline;
    justify-content: space-between;
  }
  .nutrition-facts {
    font-size: 26px;
    white-space: nowrap;
  }
  .nutrition-facts span + span {
    margin-left: 28px;
  }
  .net-weight {
    font-size: 46px;
    line-height: 1;
  }
  .brand-panel {
    flex: 1;
    height: 100%;
    background: var(--brand-blue);
    display: flex;
    align-items: center;
    justify-content: center;
  }
  .brand-name {
    margin: 0;
    color: var(--white);
    font-size: 40px;
    font-weight: 400;
    white-space: nowrap;
  }
</style>
</head>
<body>
  <div class="wrapper">
    <section class="info-panel">
      <h1 class="flavour-name">Banana Bread Flavour</h1>
      <p class="product-claims">Raw, cold pressed bar with the protein isolate<br>and prebiotic fibre.&nbsp; Natural, with no artificial<br>colours, flavours, preservatives or sweeteners.<br>No added sugar or sugar alcohols gluten free,<br>soy free.</p>
      <div class="divider"></div>
      <div class="nutrition-row">
        <div class="nutrition-facts"><span>&gt;20g Protein</span><span>&lt;3g Carbs</span><span>&lt;1g Sugar</span></div>
        <div class="net-weight">60g</div>
      </div>
    </section>
    <aside class="brand-panel">
      <p class="brand-name">Lumo Keto Bar</p>
    </aside>
  </div>
</body>
</html>
```